Brochure Design

We do residential customer home theatre installations. TV cabinet top and wall mounted installations, surround sound installations wired and wireless systems. The attached file is a brochure I have already designed and would like it to look like this, it just needs to be taken to a more professional standard.
Updates

to all designers the brochure colours are important. The complete background must be in black. The Brightlane QX logo must stay the same. The font in the description tables must be white. Basically I want the brochure to look much the same. Just enhance the tables to look more professional and improve the layout so everything lines up and it folds correctly.

regards,
Theo

Target Market(s)

mid range budget of people of all ages

Industry/Entity Type

Residential

Requirements
Must have
• I want it to look like the brochure I have provided, in a more presentable and professional manner. please keep the colour scheme as close as the original
Nice to have
• good symmetry and layout. Try and keep the font similar to the original. the pictures I have included are important.
Should not have
• do not change the colour scheme to far from the original

```html
<!DOCTYPE html>
<html lang="en">
<head>
<meta charset="utf-8">
<title>Home Theatre Installations Brochure</title>
<link href="https://fonts.googleapis.com/css2?family=Exo+2:wght@300;400&family=Arimo:wght@400;700&display=swap" rel="stylesheet">
<style>
:root{
  --band:#14a5e4;
  --ink:#ffffff;
  --rule:#1a8fd8;
  --paper:#000000;
  --head:#ffffff;
  --note:#e8f4fc;
}
*{box-sizing:border-box;margin:0;padding:0}
html,body{width:1200px;height:929px;overflow:hidden;background:var(--paper)}
body{position:relative;font-family:"Arimo",Arial,sans-serif;color:var(--ink)}
.hero{position:absolute;z-index:0}
.photo{position:absolute;z-index:1;border-radius:6px;box-shadow:0 0 5px rgba(255,255,255,.15)}
.band{position:absolute;z-index:1;background:var(--band);color:var(--head);font-family:"Exo 2",sans-serif;font-weight:300;font-size:17px;letter-spacing:1px;text-align:center;display:flex;align-items:center;justify-content:center}
table{position:absolute;z-index:1;border-collapse:collapse;font-size:9px;line-height:1.08;table-layout:fixed;color:var(--ink);background:var(--paper)}
td,th{border:1px solid var(--rule);padding:1px 3px;vertical-align:middle;font-weight:400}
th{font-weight:700;text-align:center;white-space:nowrap}
.size{text-align:center;white-space:nowrap;padding:1px 1px}
.desc-h{text-align:left}
.price{text-align:center;white-space:nowrap;padding:1px 1px}
.terms{position:absolute;z-index:1;left:847px;top:590px;width:309px;font-size:7px;line-height:1.2;color:var(--note)}
.terms h3{font-size:9px;font-weight:700;margin-bottom:6px;line-height:1.15;color:var(--ink)}
.terms p{margin-bottom:7px}
</style>
</head>
<body>

<!-- Left panel -->
<div class="photo" role="img" aria-label="Wall mounted TV with tall floor speakers in a white room" style="left:82px;top:47px;width:234px;height:129px;background:linear-gradient(180deg,#f4f4f4,#d8d8d8)"></div>
<div class="band" style="left:44px;top:192px;width:308px;height:26px">Supreme Installations Continued</div>
<table style="left:44px;top:219px;width:308px">
  <colgroup><col style="width:127px"><col style="width:61px"><col style="width:60px"><col style="width:60px"></colgroup>
  <tr style="height:15px"><th rowspan="2" class="desc-h">Description of works</th><th>TV Size</th><th>TV Size</th><th>TV Size</th></tr>
  <tr style="height:14px"><td class="size">22 – 50 inch</td><td class="size">51 – 69 inch</td><td class="size">70 – 150 inch</td></tr>
  <tr style="height:30px"><td colspan="4">Set up plasma/LCD/LED TV Wall Mounted with connection to all existing components and ...</td></tr>
  <tr style="height:58px"><td>Unlimited components - with NEW wireless 5.1 surround sound system - all speakers being on stands no concealing of speaker cables</td><td class="price">$429.00<br>MC 1</td><td class="price">$529.00<br>MC 2</td><td class="price">$629.00<br>MC 3</td></tr>
  <tr style="height:58px"><td>NEW audio component being Soundbar no concealing of speaker cables</td><td class="price">$429.00<br>MC 4</td><td class="price">$529.00<br>MC 5</td><td class="price">$629.00<br>MC 6</td></tr>
  <tr style="height:58px"><td>NEW audio component being 5.1 wireless surround sound - one set of rear speakers being mounted</td><td class="price">$579.00<br>MC 7</td><td class="price">$679.00<br>MC 8</td><td class="price">$779.00<br>MC 9</td></tr>
</table>

<div class="photo" role="img" aria-label="Home theatre room with surround speakers and armchair" style="left:82px;top:486px;width:234px;height:126px;background:linear-gradient(160deg,#f2eefb,#c9bfe6)"></div>
<div class="band" style="left:44px;top:622px;width:308px;height:28px">Premium Installations</div>
<table style="left:44px;top:651px;width:308px">
  <colgroup><col style="width:127px"><col style="width:61px"><col style="width:60px"><col style="width:60px"></colgroup>
  <tr style="height:16px"><th rowspan="2" class="desc-h">Description of works</th><th>TV Size</th><th>TV Size</th><th>TV Size</th></tr>
  <tr style="height:16px"><td class="size">22 – 50 inch</td><td class="size">51 – 69 inch</td><td class="size">70 – 150 inch</td></tr>
  <tr style="height:42px"><td colspan="4">Set up Plasma/LCD/LED TV on Cabinet with connection to all existing components and NEW hard-wired surround sound system. The below costs are based on a Theatre room size up to 20 square metres ...</td></tr>
  <tr style="height:28px"><td>Audio component being 5.1 wired surround sound</td><td class="price">$649.00<br>CC 1</td><td class="price">$729.00<br>CC 2</td><td class="price">$799.00<br>CC 3</td></tr>
  <tr style="height:28px"><td>Audio component being 7.1 wired surround sound</td><td class="price">$899.00<br>CC 4</td><td class="price">$979.00<br>CC 5</td><td class="price">$1,049.00<br>CC 6</td></tr>
  <tr style="height:44px"><td colspan="4">Set up Plasma/LCD/LED TV Wall Mounted with connection to all existing components and NEW hard-wired surround sound system. The below costs are based on a Theatre room size up to 20 square metres ...</td></tr>
  <tr style="height:29px"><td>Audio component being 5.1 wired surround sound</td><td class="price">$819.00<br>CW 1</td><td class="price">$899.00<br>CW 2</td><td class="price">$999.00<br>CW 3</td></tr>
  <tr style="height:30px"><td>Audio component being 7.1 wired surround sound</td><td class="price">$1,069.00<br>CW 4</td><td class="price">$1,149.00<br>CW 5</td><td class="price">$1,249.00<br>CW 6</td></tr>
</table>

<!-- Middle panel -->
<div class="photo" role="img" aria-label="Projector lens emitting blue light" style="left:448px;top:68px;width:140px;height:112px;background:radial-gradient(circle at 45% 50%,#8fd4ff,#123a8c 60%,#06123a)"></div>
<div class="photo" role="img" aria-label="Pull-down projector screen on blue wall" style="left:602px;top:68px;width:148px;height:112px;background:linear-gradient(90deg,#1d3f9e,#dfe4ec 20%,#f4f4f4 50%,#dfe4ec 80%,#1d3f9e)"></div>
<div class="band" style="left:446px;top:190px;width:308px;height:28px">Projector</div>
<table style="left:446px;top:221px;width:308px">
  <colgroup><col style="width:249px"><col style="width:59px"></colgroup>
  <tr style="height:60px"><td>Set up Projector on Wall or Ceiling mount, conceal cables and Calibrate with unlimited components - HD recorder/ DVD Blue ray, Streamvue or equivalent including existing surround sound 5.1 or 7.1 and soundbar</td><td class="price">Quote</td></tr>
  <tr style="height:13px"><td>Set up screen - Standard</td><td class="price">Quote</td></tr>
  <tr style="height:14px"><td>Set up screen - Motorised</td><td class="price">Quote</td></tr>
</table>

<div class="band" style="left:446px;top:323px;width:308px;height:29px">Additions</div>
<table style="left:446px;top:354px;width:308px">
  <colgroup><col style="width:249px"><col style="width:59px"></colgroup>
  <tr style="height:29px"><td colspan="2">Additional items installed with another purchase- original purchase being TV and sound system</td></tr>
  <tr style="height:44px"><td>Set up 5.1 wireless surround sound system and connect to all existing components including Plasma/LCD/LED TV cabinet top.</td><td class="price">$159.00<br>AS 1</td></tr>
  <tr style="height:44px"><td>Set up 5.1 wireless surround sound system and connect to all existing components including Plasma/LCD/LED TV on cabinet any size with one set of speakers being mounted</td><td class="price">$289.00<br>AM 1</td></tr>
  <tr style="height:44px"><td>Set up 5.1 wireless surround sound system and connect to all existing components including Plasma/LCD/LED TV Wall Mounted</td><td class="price">$229.00<br>AS 1</td></tr>
  <tr style="height:44px"><td>Set up 5.1 wireless surround sound system and connect to all existing components including Plasma/LCD/LED TV Wall Mounted any size with one set of speakers being mounted</td><td class="price">$369.00<br>AM 2</td></tr>
  <tr style="height:44px"><td>Set up Soundbar - connect to Cabinet or Wall mounted TV (cable concealing not included)</td><td class="price">$189.00<br>AM 3</td></tr>
  <tr style="height:22px"><td>Set up personal video recorder</td><td class="price">$99.00<br>AS 3</td></tr>
  <tr style="height:22px"><td>Set up personal video recorder with network connection</td><td class="price">$199.00<br>AS 4</td></tr>
</table>

<div class="photo" role="img" aria-label="Rooftop TV antenna against blue sky" style="left:485px;top:666px;width:230px;height:112px;background:linear-gradient(180deg,#3f6fc9,#9cc3ef)"></div>
<div class="band" style="left:446px;top:788px;width:308px;height:28px">Antennas</div>
<table style="left:446px;top:818px;width:308px">
  <colgroup><col style="width:249px"><col style="width:59px"></colgroup>
  <tr style="height:22px"><td>Analyse digital reception</td><td class="price">$99.00<br>AS 5</td></tr>
  <tr style="height:22px"><td>Upgrade antenna to digital</td><td class="price">$299.00<br>AS 6</td></tr>
  <tr style="height:23px"><td>New antenna with one point provided</td><td class="price">$399.00<br>AS 7</td></tr>
</table>

<!-- Right panel -->
<div class="hero" role="img" aria-label="Large flat screen TV on a low cabinet in a warmly lit living room" style="left:760px;top:0;width:440px;height:440px;background:linear-gradient(90deg,rgba(0,0,0,0) 0%,rgba(120,80,70,.6) 25%,rgba(170,130,125,.8) 55%,rgba(140,120,175,.85) 85%,rgba(110,140,200,.9) 100%);-webkit-mask-image:linear-gradient(180deg,#000 70%,transparent);mask-image:linear-gradient(180deg,#000 70%,transparent)"></div>
<div class="photo" role="img" aria-label="Black glass TV cabinet" style="left:850px;top:320px;width:305px;height:102px;background:linear-gradient(180deg,#f6f6f6,#cfcfcf)"></div>
<div class="band" style="left:847px;top:437px;width:309px;height:28px">Cabinet Assembly</div>
<table style="left:847px;top:467px;width:309px">
  <colgroup><col style="width:249px"><col style="width:60px"></colgroup>
  <tr style="height:22px"><td>Cabinet – assemble small – medium - cabinet</td><td class="price">$109.00<br>AS 8</td></tr>
  <tr style="height:22px"><td>Cabinet – assemble large cabinet</td><td class="price">$169.00<br>AS 9</td></tr>
</table>
<div class="band" style="left:847px;top:512px;width:309px;height:28px">Concealing Cables</div>
<table style="left:847px;top:542px;width:309px">
  <colgroup><col style="width:249px"><col style="width:60px"></colgroup>
  <tr style="height:23px"><td>Supply and install cable duct 40mm X 25mm exposed (per metre)</td><td class="price">$49.00<br>AS 10</td></tr>
</table>

<div class="terms">
  <h3>Terms and conditions – Notes<br>All pricing based on</h3>
  <p>All costing is based on one single storey dwelling with tiled roof. Allowing access both to ceiling space and all wall cavities.</p>
  <p>Description – Wall Mounted – all wall mounts pricing includes concealing cable through wall cavity where access can be gained. If no access e.g. internal walls, the required cable ducting can be purchased from the installer.</p>
  <p>All surround sound pricing is based on speaker wire of specifications 2 core 14/0.14 mmsq. Speaker cable upgrade is available to be purchased from the installer at the time of installation.</p>
  <p>Dwelling must not contain asbestos. On arrival if the dwelling contains asbestos the installer will not continue and will leave site immediately. NO refunds given.</p>
  <p>All existing interconnecting cables are to be correct length and in good working condition.</p>
  <p>All interconnecting cables and mounting products and their brackets for televisions and speakers for the installation are to be supplied by customer.</p>
  <p>Additional cables required for installation not supplied by the customer – may be purchased directly from the installer and payment made at the time of purchase from installer.</p>
  <p>All General Power Outlets (GPO) must exist if additional power outlets are required – it is not included in the pricing. If the installer is a licensed electrician additional outlets may be purchased at the time of installation for an additional cost.</p>
  <p>All existing components including surround sound must be in good condition / working order. Free to air reception must be in acceptable quality for the installation. If reception is of poor quality it is up to the customer to arrange rectification / new antenna.</p>
  <p>For wall mounted units wall cavity enclosures can be purchased from the installer if required.</p>
  <p>The above pricing is based on all components being compatible with purchase, if not the installer may be able to solve the problem at an additional cost.</p>
</div>

</body>
</html>
```